Brindle Outcomes WebDesign

Although the designs we have had are great we are looking for something unique and would like to move away from the traditional. We append additional comments and files to reflect this. WE are looking for designs to showcase there artistic flare.

Task
To design Brindle Outcomes home page and a second page ie information on our Internet Marketing Services

Client:
Brindle Outcomes is the next generation provider of international marketing, branding, design, Search Engine Optimization(SEO) and Search Engine Marketing(SEM). Utilising a variety of crowd-source channels and trust networks, Brindle Outcomes is able to offer you a complete internet marketing package. From initial design and branding to the continued work on SEO all our services are geared towards dramatically increasings your revenues. Our primary goal is to build greater trading bridges between English-speaking and Chinese-speaking worlds. We believe that a true understanding of the local market is only achievable if you are a native speaker. The power of our networks and processes have been focused to enable Brindle Outcomes to enlist only native speakers to bolster your Internet Marketing Campaign.

The primary color pallet is:

FF9571
B23308
FF6633
858585
BDBDBD
or
https://palettes.vormix.example/#themes/search?term=brindle%20outcomes

Sites we like
http://www.trevonix.example/
http://www.morbela.example/
Updates

We have believe that we will need to push our design packages (outsourced through artflockly) more. We would like this to be reflected on the front page.

This means that the menu should also include

Design
Also the use of content management system wendix

Have added a few more sites that we like
www.harbourpixelstudio.example.hk
www.qmt.example.hk

Really excited with all the designs so far.  We would like the design to move away from the more standard layout. With this in mind we would like to see some design that feature hexagons, or decagons.
Please feel free to let loose! we want a design that is quit unique

We have included to vector files.

vector file 8016151 is for a color reference we thik that in order to enhence the design we need to expand the color palette, would want to maintain the primary corporate colors, but include some bright additional colors.

The second was our insipration for the the hexagon. expanding on the idea we thought that the main menu could be made up of hexagons. The ad/info modules that appear half way up the page be similar to those in the vector.

Reason: Have updated brief and are looking for a more unique feel to the design.

Target Market(s)

Small to medium business looking to branch out further in the international market

Industry/Entity Type

Internet

Requirements
Must have
• A login/search section
A separate floating feedback tab
Main Navigation – Home, Internet Marketing, Cloud Computing
A banner space from informative text on our services
Must have a request for a quote on each page

```html
<!DOCTYPE html>
<html lang="en">
<head>
<meta charset="utf-8">
<title>Brindle Outcomes – SEO and Cloud Consultant</title>
<link rel="stylesheet" href="https://fonts.googleapis.com/css2?family=Open+Sans:wght@400;600;700&family=Oswald:wght@600&family=Roboto+Condensed:ital,wght@0,400;0,700;1,300&family=Arimo&display=swap">
<style>
:root{
  --page:#f4f4f4;
  --orange:#ff6633;
  --orange-deep:#f26522;
  --rust:#b23308;
  --salmon:#ff9571;
  --yellow:#ffd21a;
  --grey-dark:#858585;
  --grey:#bdbdbd;
  --grey-panel:#b7b7b7;
  --grey-head:#c4c4c4;
  --green:#2e9e3a;
  --purple:#9b3fa0;
  --blue:#1d74c0;
  --royal:#1f47b0;
  --text-dark:#555;
  --white:#fff;
}
*{box-sizing:border-box;margin:0;padding:0}
html,body{width:1007px;height:1200px;overflow:hidden;background:var(--page)}
body{position:relative;font-family:"Open Sans",sans-serif;color:var(--text-dark)}
.abs{position:absolute}
.stage{position:absolute;left:0;top:0}

/* header */
.brand{left:45px;top:19px;display:flex;align-items:center}
.brand-ring{width:74px;height:74px;border-radius:50%;border:7px solid var(--orange)}
.brand-name{position:absolute;left:85px;top:6px;font-family:"Open Sans",sans-serif;font-weight:700;font-size:33px;letter-spacing:-.5px;color:var(--orange);white-space:nowrap}
.brand-tag{position:absolute;left:120px;top:51px;font-size:12.5px;color:#222;white-space:nowrap}

.nav-hex{position:absolute;height:43px;display:flex;align-items:center;justify-content:center;font-family:"Roboto Condensed",sans-serif;font-weight:700;font-size:14.5px;color:#3a3a3a}
.nav-hex svg{position:absolute;inset:0}
.nav-hex span{position:relative}
.search span{font-family:"Open Sans",sans-serif;font-weight:400;font-size:11px;color:#555;margin-right:54px}
.search .lens{position:absolute;right:18px;top:14px;width:14px;height:14px}

/* banner text */
.headline{right:57px;top:180px;font-family:"Oswald",sans-serif;font-weight:600;font-size:41px;letter-spacing:.5px;color:#c8380c;white-space:nowrap}
.tagline{font-family:"Roboto Condensed",sans-serif;font-style:italic;font-weight:300;font-size:58px;color:var(--white);white-space:nowrap;line-height:1}
.tagline.one{left:568px;top:276px}
.tagline.two{left:674px;top:324px}

/* service hexes */
.svc-title{font-size:16.5px;font-weight:600;letter-spacing:.3px;text-align:center;width:240px}
.svc-title.web{left:79px;top:551px;color:#1b3aa8;font-weight:700}
.svc-title.brand-t{left:388px;top:551px;color:#8a8a8a}
.svc-title.mkt{left:697px;top:550px;color:#8a8a8a}
.svc-blurb{left:74px;top:640px;width:250px;text-align:center;font-size:12px;line-height:17.4px;color:var(--white)}

/* panels */
.panel-title{font-size:18px;font-weight:600;color:#666}
.welcome-title{left:89px;top:812px}
.welcome-body{left:67px;top:850px;width:562px;font-size:12px;line-height:17.4px;color:var(--white);text-align:justify;height:168px;overflow:hidden}
.welcome-body p+p{margin-top:11px}
.read-more{left:538px;top:1026px;font-size:11px;color:#555}
.quote-title{left:713px;top:812px}
.field{position:absolute;left:689px;width:259px;height:22px;background:#c9c9c9;border:1px solid #9e9e9e;border-top:2px solid #8e8e8e;font-size:10.5px;color:#555;padding:3px 7px;font-family:"Open Sans",sans-serif}
.field.remarks{height:50px}
.submit{left:863px;top:1023px;width:63px;height:23px;background:#6f6f6f;border:2px solid #e6e6e6;border-radius:3px;color:var(--white);font-size:12px;font-weight:700;letter-spacing:.4px;display:flex;align-items:center;justify-content:center;box-shadow:0 0 0 1px #9a9a9a}

/* footer */
.foot-links{left:45px;top:1151px;font-family:"Arimo",sans-serif;font-size:11px;color:#777}
.foot-links .policy{color:var(--orange)}
.foot-links .sep{color:#bbb;margin:0 6px}
.legal{left:0;width:1012px;top:1151px;text-align:center;font-family:"Arimo",sans-serif;font-size:11px;color:#777}
</style>
</head>
<body>

<svg class="stage" width="1007" height="1200" viewBox="0 0 1007 1200" aria-hidden="false">
  <defs>
    <linearGradient id="bannerFill" x1="0" y1="0" x2="1" y2="0">
      <stop offset="0" stop-color="#ff7a1a"/>
      <stop offset=".45" stop-color="#ffb41a"/>
      <stop offset=".75" stop-color="#ffc91c"/>
      <stop offset="1" stop-color="#ff8a1a"/>
    </linearGradient>
    <linearGradient id="hexOrange" x1="0" y1="0" x2="1" y2="1">
      <stop offset="0" stop-color="#ffb300"/>
      <stop offset="1" stop-color="#f2560f"/>
    </linearGradient>
    <linearGradient id="greyRing" x1="0" y1="0" x2="1" y2="1">
      <stop offset="0" stop-color="#a8a8a8"/>
      <stop offset="1" stop-color="#8a8a8a"/>
    </linearGradient>
    <linearGradient id="blueRing" x1="0" y1="0" x2="1" y2="1">
      <stop offset="0" stop-color="#2a6fd6"/>
      <stop offset="1" stop-color="#1a2f96"/>
    </linearGradient>
    <linearGradient id="photoTone" x1="0" y1="0" x2="0" y2="1">
      <stop offset="0" stop-color="#e7e2de"/>
      <stop offset="1" stop-color="#8f8a88"/>
    </linearGradient>
    <linearGradient id="greyTone" x1="0" y1="0" x2="0" y2="1">
      <stop offset="0" stop-color="#d6d6d6"/>
      <stop offset="1" stop-color="#8c8c8c"/>
    </linearGradient>
    <clipPath id="webInner"><polygon points="74,633 136.5,524.7 261.5,524.7 324,633 261.5,741.3 136.5,741.3"/></clipPath>
  </defs>

  <!-- banner -->
  <g class="banner">
    <polygon points="72,143 978,143 1012,176 1012,448 980,480 74,480 39,448 39,176" fill="#ececec" stroke="#e2e2e2"/>
    <polygon points="75,147 975,147 972,147 1008,183 1008,445 975,476 76,476 43,445 43,180" fill="url(#bannerFill)"/>
    <polygon points="93,282 180.5,130.4 355.5,130.4 443,282 355.5,433.6 180.5,433.6" fill="url(#hexOrange)"/>
    <polygon points="108,282 188,143.4 348,143.4 428,282 348,420.6 188,420.6" fill="#ff8a1e"/>
    <polygon points="128,282 198,160.8 338,160.8 408,282 338,403.2 198,403.2" fill="#fbfbfb"/>
    <g role="img" aria-label="Photo of a young woman with headphones lying on the floor using a laptop">
      <polygon points="142,282 205,172 331,172 394,282 331,392 205,392" fill="url(#photoTone)" opacity=".55"/>
    </g>
  </g>

  <!-- large service hexagons -->
  <g class="svc web">
    <polygon points="46,633 122.5,500.5 275.5,500.5 352,633 275.5,765.5 122.5,765.5" fill="url(#blueRing)"/>
    <polygon points="74,633 136.5,524.7 261.5,524.7 324,633 261.5,741.3 136.5,741.3" fill="#fff"/>
    <g role="img" aria-label="Illustration of pen nib, paintbrushes and paint tubes">
      <rect x="150" y="572" width="100" height="62" rx="10" fill="#4e5f86" opacity=".55"/>
    </g>
    <g clip-path="url(#webInner)">
      <rect x="60" y="632" width="280" height="120" fill="#3650c8" opacity=".78"/>
    </g>
  </g>
  <g class="svc branding">
    <polygon points="355,633 431.5,500.5 584.5,500.5 661,633 584.5,765.5 431.5,765.5" fill="url(#greyRing)"/>
    <polygon points="383,633 445.5,524.7 570.5,524.7 633,633 570.5,741.3 445.5,741.3" fill="#fff"/>
    <g role="img" aria-label="Grey rubber stamp illustration reading branding">
      <circle cx="511" cy="660" r="67" fill="url(#greyTone)" opacity=".7"/>
    </g>
  </g>
  <g class="svc marketing">
    <polygon points="664,633 740.5,500.5 893.5,500.5 970,633 893.5,765.5 740.5,765.5" fill="url(#greyRing)"/>
    <polygon points="692,633 754.5,524.7 879.5,524.7 942,633 879.5,741.3 754.5,741.3" fill="#fff"/>
    <g role="img" aria-label="3D grey SEO letters with rising arrows">
      <rect x="762" y="590" width="118" height="130" rx="12" fill="url(#greyTone)" opacity=".7"/>
    </g>
  </g>

  <!-- small hexagons -->
  <g class="mini">
    <polygon points="445,340 473.5,290.6 530.5,290.6 559,340 530.5,389.4 473.5,389.4" fill="url(#hexOrange)"/>
    <g role="img" aria-label="Small photo of woman with laptop">
      <polygon points="458,340 480,301.9 524,301.9 546,340 524,378.1 480,378.1" fill="url(#photoTone)"/>
    </g>

    <polygon points="531,392 561,340 621,340 651,392 621,444 561,444" fill="url(#greyRing)"/>
    <g role="img" aria-label="Photo of a tablet and a smartphone">
      <polygon points="545,392 568,352.2 614,352.2 637,392 614,431.8 568,431.8" fill="#f4f4f4"/>
      <rect x="574" y="366" width="28" height="40" rx="3" fill="#3a3a3a" opacity=".6"/>
    </g>

    <polygon points="440,447 470,395 530,395 560,447 530,499 470,499" fill="url(#greyRing)"/>
    <g role="img" aria-label="Photo of a silver sports car">
      <polygon points="454,447 477,407.2 523,407.2 546,447 523,486.8 477,486.8" fill="#f4f4f4"/>
      <ellipse cx="500" cy="447" rx="34" ry="14" fill="#9a9a9a" opacity=".55"/>
    </g>

    <polygon points="282,510 317,449.4 387,449.4 422,510 387,570.6 317,570.6" fill="url(#greyRing)"/>
    <g role="img" aria-label="Illustration of a shopping cart and computer mouse">
      <polygon points="297,510 324.5,462.4 379.5,462.4 407,510 379.5,557.6 324.5,557.6" fill="#f2f2f2"/>
      <rect x="322" y="488" width="48" height="34" rx="5" fill="#aaa" opacity=".5"/>
    </g>

    <polygon points="592,510 627,449.4 697,449.4 732,510 697,570.6 627,570.6" fill="url(#greyRing)"/>
    <g role="img" aria-label="Photo of a smiling businesswoman with arms folded">
      <polygon points="607,510 634.5,462.4 689.5,462.4 717,510 689.5,557.6 634.5,557.6" fill="url(#photoTone)" opacity=".7"/>
    </g>
  </g>

  <!-- welcome panel -->
  <g class="welcome-panel">
    <polygon points="80,803 617,803 650,836 650,1030 624,1056 72,1056 46,1030 46,841" fill="var(--grey-panel)"/>
    <polygon points="80,803 617,803 650,836 650,841 46,841" fill="var(--grey-head)"/>
    <line x1="46" y1="841" x2="650" y2="841" stroke="#a5a5a5"/>
  </g>

  <!-- quote panel -->
  <polygon class="quote-panel" points="702,803 936,803 969,836 969,1030 943,1056 695,1056 669,1030 669,836" fill="var(--grey-panel)"/>

  <!-- footer rule and mark -->
  <line x1="60" y1="1115" x2="470" y2="1115" stroke="#dedede"/>
  <line x1="534" y1="1115" x2="950" y2="1115" stroke="#dedede"/>
  <circle cx="502" cy="1115" r="22" fill="none" stroke="#8d8d8d" stroke-width="4"/>

  <!-- social buttons -->
  <g class="social">
    <circle cx="826" cy="1156" r="13" fill="#33b5e8" stroke="#d9d9d9" stroke-width="2"/>
    <circle cx="858" cy="1156" r="13" fill="#a3a3a3" stroke="#d9d9d9" stroke-width="2"/>
    <circle cx="890" cy="1156" r="13" fill="#a3a3a3" stroke="#d9d9d9" stroke-width="2"/>
    <circle cx="922" cy="1156" r="13" fill="#a3a3a3" stroke="#d9d9d9" stroke-width="2"/>
    <circle cx="953" cy="1156" r="13" fill="#a3a3a3" stroke="#d9d9d9" stroke-width="2"/>
  </g>
</svg>

<!-- header -->
<header>
  <div class="abs brand">
    <div class="brand-ring"></div>
    <div class="brand-name">BrindleOutcomes.com</div>
    <div class="brand-tag">SEO and Cloud Consultant</div>
  </div>

  <nav>
    <a class="nav-hex" style="left:449px;top:58px;width:66px">
      <svg width="66" height="43" viewBox="0 0 66 43"><polygon points="3,21.5 14,3 52,3 63,21.5 52,40 14,40" fill="#fff" stroke="var(--green)" stroke-width="5"/></svg>
      <span>Home</span>
    </a>
    <a class="nav-hex" style="left:507px;top:36px;width:133px">
      <svg width="133" height="43" viewBox="0 0 133 43"><polygon points="3,21.5 14,3 119,3 130,21.5 119,40 14,40" fill="#fff" stroke="var(--orange-deep)" stroke-width="5"/></svg>
      <span>Internet Marketing</span>
    </a>
    <a class="nav-hex" style="left:632px;top:58px;width:130px">
      <svg width="130" height="43" viewBox="0 0 130 43"><polygon points="3,21.5 14,3 116,3 127,21.5 116,40 14,40" fill="#fff" stroke="var(--orange-deep)" stroke-width="5"/></svg>
      <span>Cloud Computing</span>
    </a>
    <a class="nav-hex" style="left:755px;top:36px;width:72px">
      <svg width="72" height="43" viewBox="0 0 72 43"><polygon points="3,21.5 14,3 58,3 69,21.5 58,40 14,40" fill="#fff" stroke="var(--orange-deep)" stroke-width="5"/></svg>
      <span>Contact</span>
    </a>
    <div class="nav-hex search" style="left:821px;top:12px;width:148px">
      <svg width="148" height="43" viewBox="0 0 148 43"><polygon points="3,21.5 14,3 134,3 145,21.5 134,40 14,40" fill="#fff" stroke="var(--purple)" stroke-width="5"/></svg>
      <span>Search</span>
      <svg class="lens" viewBox="0 0 14 14"><circle cx="5.5" cy="5.5" r="4" fill="none" stroke="#444" stroke-width="1.8"/><line x1="8.5" y1="8.5" x2="13" y2="13" stroke="#444" stroke-width="2.2"/></svg>
    </div>
    <a class="nav-hex" style="left:820px;top:58px;width:65px">
      <svg width="65" height="43" viewBox="0 0 65 43"><polygon points="3,21.5 14,3 51,3 62,21.5 51,40 14,40" fill="#fff" stroke="var(--blue)" stroke-width="5"/></svg>
      <span>Login</span>
    </a>
    <a class="nav-hex" style="left:875px;top:81px;width:86px">
      <svg width="86" height="43" viewBox="0 0 86 43"><polygon points="3,21.5 14,3 72,3 83,21.5 72,40 14,40" fill="#fff" stroke="var(--blue)" stroke-width="5"/></svg>
      <span>Register</span>
    </a>
  </nav>
</header>

<!-- banner copy -->
<section class="hero">
  <h1 class="abs headline">WE ENJOY BIG CHALLENGES</h1>
  <div class="abs tagline one">Lorem Ipsum</div>
  <div class="abs tagline two">Lorem Ipsum</div>
</section>

<!-- services -->
<section class="services">
  <h2 class="abs svc-title web">WEBSITE DESIGN</h2>
  <p class="abs svc-blurb">tetur adipiscing elit. Donec eleifend, lo<br>Lorem ipsum dolor sit amet, cons<br>Lorem ipsum dolor sit amet,<br>Lorem ipsum dolor sit am<br>Lorem ipsum dolor sit</p>
  <h2 class="abs svc-title brand-t">BRANDING</h2>
  <h2 class="abs svc-title mkt">E-MARKETING</h2>
</section>

<!-- welcome -->
<section class="welcome">
  <h3 class="abs panel-title welcome-title">Welcome Brindle Outcomes</h3>
  <div class="abs welcome-body">
    <p>Lorem Ipsum is simply dummy text of the printing and typesetting industry. Lorem Ipsum has been the industry's standard dummy text ever since the 1500s, when an unknown printer took a galley of type and scrambled it to make a type specimen book.</p>
    <p>It has survived not only five centuries, but also the leap into electronic typesetting, remaining essentially unchanged. It was popularised in the 1960s with the release of Typeleaf sheets containing Lorem Ipsum passages, and more recently with desktop publishing software like Quillpage Composer including versions of Lorem Ipsum.Lorem Ipsum is simply dummy text of the printing and typesetting industry. Lorem Ipsum has been the industry's standard dummy text ever since the 1500s, when an unknown printer took a galley of type and scrambled it to make a type specimen book. It has survived not only five centuries,</p>
  </div>
  <a class="abs read-more">Read more &gt;&gt;</a>
</section>

<!-- quote -->
<section class="quote">
  <h3 class="abs panel-title quote-title">Request a Quote</h3>
  <div class="field" style="top:848px">Your Name</div>
  <div class="field" style="top:887px">Your Email</div>
  <div class="field" style="top:925px">Your Phone</div>
  <div class="field remarks" style="top:964px">Remarks</div>
  <div class="abs submit">SUBMIT</div>
</section>

<!-- footer -->
<footer>
  <div class="abs foot-links"><span class="policy">Privacy Policy</span><span class="sep">/</span>Terms</div>
  <div class="abs legal">© 2012-2013 Brindle Outcomes.com. All rights reserved.</div>
</footer>

</body>
</html>
```